Fun but professional website required for school teaching consultancy.

Dear Designers,

I have an interesting brief for you. My client is a skilled teacher who is looking to promote her consultancy that provides bespoke training and support to other teachers.

She would like a website that promotes her philosophy for working with children, which is essentially that she wants to create a fun and creative learning environment for them, whilst maintaining the professionalism that is also required to succeed. Representation of the balance between these two points is crucial to the design.

Typically these kind of websites are pretty boring so we need something fun and vibrant, not uninviting ie those typical images of a teacher sat behind a desk or anything overly formal.

Here is an example of what we do not want: http://www.brightmarrowlearning.co.uk/ - in this one although my client liked the layout, she hated the graphics.

Here is a website that she really liked and captured the vibe of what she is trying to promote about herself: http://www.pellowfieldkidsplace.com/ - this design indicates fun with learning, happy kids, lively colours and still has a professional feel as well.

If you have any further questions, please ask

Many thanks,

Garth

PS Enclosed please find a whole bunch of resources (including site map) for this project. My client has supplied graphics, page content and plenty of visuals so hopefully this will make things easier
Updates

To all designers,

Thanks all your designs. Just to let you all know they have been sent to the client and I will supply feedback to you all individually when I get it.

Many thanks,
Garth

Hi all,

We've had loads of designs for this project so thanks to you all very much. If there is any feedback to pass on, I will do this directly. Right now, all designs have been liked and are in the running. My client is going through them all and will make a decision on the deadline date which is the 10th May.
If you don't hear from me before then, it's simply because no alterations have been requested.

Many thanks.
Garth

Industry/Entity Type

Training

```html
<!DOCTYPE html>
<html lang="en">
<head>
<meta charset="utf-8">
<title>Keystone Learning Consultancy</title>
<link href="https://fonts.googleapis.com/css2?family=Schoolbell&family=Ubuntu:wght@400;500&display=swap" rel="stylesheet">
<style>
:root{
  --sky:#2fa6d6; --sky-light:#46c0f4; --orange:#ffa200; --lime:#9cc22b; --red:#e0361a;
  --cyan:#3ddcf7; --yellow:#ffbd0b; --pink:#e5179b; --blue-head:#1b8be0; --magenta:#d41cc4;
  --green:#2eb62e; --contact:#4cbf3b; --teal:#47dbb4; --panel:#f1f1ec; --text:#222;
}
*{box-sizing:border-box;margin:0;padding:0}
html,body{width:1045px;height:1200px;overflow:hidden;background:#fff}
body{position:relative;font-family:'Ubuntu',sans-serif;color:var(--text)}
.site-header{position:absolute;left:0;top:0;width:1045px;height:154px;background:linear-gradient(var(--sky),var(--sky-light))}
.brand{position:absolute;left:164px;top:17px;width:82px;height:118px;background:#fff;border:2px solid #dfe9f0;display:flex;flex-direction:column;align-items:center;justify-content:center;gap:8px;padding:4px}
.brand-mark{width:30px;height:30px;background:var(--blue-head)}
.brand-name{font-size:9px;color:#2b5f99;text-align:center;line-height:1.3;font-family:'Ubuntu',sans-serif}
.contact-line{position:absolute;right:165px;top:14px;text-align:left;color:#fff;font-size:17px;line-height:21px}
.contact-line .phone{letter-spacing:5px}
.contact-line a{color:#fff}
.main-nav{position:absolute;left:419px;top:70px;display:flex}
.main-nav a{width:77px;height:74px;display:flex;align-items:center;justify-content:center;text-align:center;color:#fff;font-family:Arial,sans-serif;font-size:11px;text-decoration:none;line-height:14px}
.slider{position:absolute;left:164px;top:176px;width:521px;height:269px;background:linear-gradient(135deg,#3f5a2a,#8a9a5a 45%,#c8b8a0 70%,#4e6a36)}
.slider-caption{position:absolute;left:0;bottom:0;width:100%;height:55px;background:rgba(0,0,0,.6);display:flex;align-items:center;justify-content:space-between;padding:0 15px 0 26px}
.slider-caption p{color:#fff;font-size:13.5px}
.learn-more{background:#47dbb4;border:2px dashed #fff;color:#123;font-family:'Schoolbell',cursive;font-size:15px;padding:4px 6px}
.side-panel{position:absolute;left:692px;top:176px;width:188px;height:269px;background:var(--red);color:#fff;padding:10px 12px}
.side-panel h3{font-family:'Schoolbell',cursive;font-weight:400;font-size:17px;text-align:center}
.hours{width:100%;font-size:9px;margin:8px 0 6px;border-collapse:collapse}
.hours td{padding:1.5px 0}
.divider{border-top:1px dashed #fff;width:115px;margin:6px auto 10px}
.blog-text{font-size:9px;line-height:13.5px;margin-top:6px}
.read-more{font-family:'Schoolbell',cursive;font-size:11px;text-align:right;margin-top:14px}
.bubbles{position:absolute;left:688px;top:426px}
.intro{position:absolute;left:164px;top:496px;width:716px;text-align:center}
.welcome{font-family:'Schoolbell',cursive;font-weight:400;color:var(--blue-head);font-size:24px;margin-top:4px}
.section-title{font-weight:400;font-size:22px;margin-bottom:8px}
.what{position:absolute;left:178px;top:566px;width:684px}
.philosophy{position:absolute;left:178px;top:709px;width:684px}
.what .section-title{color:var(--magenta);text-align:center}
.philosophy .section-title{color:var(--green);text-align:center}
.body-copy{font-size:10.2px;line-height:13.4px;text-align:left}
.body-copy .hl{color:var(--magenta)}
.info-box{position:absolute;left:164px;width:716px;background:var(--panel)}
.contact-box{top:841px;height:162px;border-bottom:3px dotted var(--contact)}
.quote-box{top:1035px;height:132px;border-bottom:3px dotted var(--teal)}
.box-tab{position:absolute;left:0;top:0;color:#fff;font-size:14.5px;padding:8px 13px;border-bottom:3px dotted #fff}
.contact-box .box-tab{background:var(--contact);width:108px}
.quote-box .box-tab{background:var(--teal);width:216px}
.contact-list{position:absolute;left:16px;top:56px;list-style:none;font-size:11.5px}
.contact-list li{display:flex;align-items:center;gap:12px;height:27px}
.contact-list svg{width:18px;height:18px}
.quote{position:absolute;left:0;top:55px;width:716px;display:flex;align-items:center;justify-content:space-between;padding:0 45px}
.quote-mark{font-family:Georgia,serif;font-size:110px;color:#c8c8c2;line-height:1;height:60px;margin-top:-10px}
.quote p{font-size:22px;color:#222}
.site-footer{position:absolute;left:164px;top:1180px;width:716px;display:flex;justify-content:space-between;font-size:8.5px}
</style>
</head>
<body>
<header class="site-header">
  <div class="brand"><span class="brand-mark"></span><span class="brand-name">Keystone Learning Ltd.</span></div>
  <div class="contact-line"><div class="phone">Call us on : 07700 900418</div><div>Email: <a href="#">enquiries@keystonelearningco.com</a></div></div>
  <nav class="main-nav">
    <a href="#" style="background:var(--orange)">Courses</a>
    <a href="#" style="background:var(--lime)">Consultant<br>Biopics</a>
    <a href="#" style="background:var(--red)">Yoga</a>
    <a href="#" style="background:var(--cyan)">T &amp; L Services</a>
    <a href="#" style="background:var(--yellow)">Resources</a>
    <a href="#" style="background:var(--pink)">PE Services</a>
  </nav>
</header>

<section class="slider" role="img" aria-label="Photo of three children examining a large leaf outdoors">
  <div class="slider-caption"><p>Slider text will come here.</p><span class="learn-more">Learn More...</span></div>
</section>

<aside class="side-panel">
  <h3>KLC Opening Time</h3>
  <table class="hours">
    <tr><td>Monday</td><td>9.00 am till 3.00pm</td></tr>
    <tr><td>Tuesday</td><td>9.00 am till 3.00pm</td></tr>
    <tr><td>Wednesday</td><td>9.00 am till 3.00pm</td></tr>
    <tr><td>Thrusday</td><td>9.00 am till 3.00pm</td></tr>
    <tr><td>Friday</td><td>9.00 am till 3.00pm</td></tr>
  </table>
  <div class="divider"></div>
  <h3>From the Blog</h3>
  <p class="blog-text">Latest Blog post will show hereLatest Blog post will show hereLatest Blog post will show hereLatest Blog post will show hereLatest Blog post will show hereLatest Blog post will show here</p>
  <p class="read-more">Read more..</p>
</aside>
<svg class="bubbles" width="80" height="42" viewBox="0 0 80 42"><circle cx="20" cy="21" r="19" fill="#e04e2e" stroke="#fff" stroke-width="3"/><circle cx="53" cy="14" r="14" fill="#e04e2e" stroke="#fff" stroke-width="3"/></svg>

<div class="intro"><h1 class="welcome">Welcome to Keystone Learning Consultancy</h1></div>

<section class="what">
  <h2 class="section-title">What we Do</h2>
  <p class="body-copy">Keystone Learning Consultancy specialises in providing bespoke <span class="hl">Teaching and Learning</span> and <span class="hl">Physical Education</span> support to the primary education sector. We offer a range of training and support methods, including team teaching, INSET, <span class="hl">courses,</span> coaching, mentoring, staff meetings and so on. Working with a diverse range of clients, such as individual primary and secondary schools, clusters, Westvale County Council, School Sports Partnerships, collaborations and Sports Coaches, we are committed to providing professional development that has a real impact on school improvement.<span class="hl">Our consultants</span> all bring with them a raft of experience in Primary Education, Physical Education and School Improvement, plus the skills to inspire and enthuse teachers.</p>
</section>

<section class="philosophy">
  <h2 class="section-title">Our Philosophy</h2>
  <p class="body-copy">We are passionate about teaching and learning - both ours and yours! We strive to practice what we preach and ensure that all our training and support is personalised for the group or individual that it is created for. We also know that our support is only as good as our own understanding, so we are dedicated to ensuring our own professional development and constantly reviewing and developing our practice. We work in partnership with our clients to design bespoke professional development opportunities, constantly reviewing and developing the support with the client to ensure their requirements are met.</p>
</section>

<section class="info-box contact-box">
  <div class="box-tab">Contact Us:</div>
  <ul class="contact-list">
    <li><svg viewBox="0 0 20 20"><path d="M5 2l3 4-2 2c1 3 3 5 6 6l2-2 4 3-2 3C9 18 2 11 2 4z" fill="#333"/></svg>Call : 07700 900418</li>
    <li><svg viewBox="0 0 20 20"><rect x="2" y="5" width="16" height="11" fill="none" stroke="#333" stroke-width="1.5"/><path d="M2 5l8 6 8-6" fill="none" stroke="#333" stroke-width="1.5"/></svg>Email : enquiries@keystonelearningco.co.uk</li>
    <li><svg viewBox="0 0 20 20"><path d="M10 1a6 6 0 0 0-6 6c0 5 6 12 6 12s6-7 6-12a6 6 0 0 0-6-6z" fill="#222"/><circle cx="10" cy="7" r="2.3" fill="#4cbf3b"/></svg>Office: Suite 4 Marlow House, 12 Ferris Lane, Hadley, Kent. ME9 2QT</li>
  </ul>
</section>

<section class="info-box quote-box">
  <div class="box-tab">Quote of the Day:</div>
  <div class="quote"><span class="quote-mark">&ldquo;</span><p>A teacher explains, a great teacher inspires.</p><span class="quote-mark">&rdquo;</span></div>
</section>

<footer class="site-footer"><span>Copyright @ Suite 4 Marlow House, 12 Ferris Lane, Hadley, Kent. ME9 2QT</span><span>enquiries@keystonelearningco.co.uk</span></footer>
</body>
</html>
```